This is a laser engraving business. I’m looking for a business card that includes a minimalist laser logo/design with the company name Brindle Crafts and telephone number 321-555-0148 and email brindlecrafts@mailbox.example

Industry/Entity Type

Laser engraving

Contact Information for Business Card

Laser logo/design that represents laser engraving

```html
<!DOCTYPE html>
<html lang="en">
<head>
<meta charset="utf-8">
<title>Brindle Crafts – Business Card</title>
<link rel="stylesheet" href="https://fonts.googleapis.com/css2?family=Montserrat:wght@300;400;700;800&display=swap">
<style>
  :root {
    --backdrop: #3b3b3d;
    --card: #0a0a0b;
    --brand-red: #d8141c;
    --accent-blue: #1f5fb4;
    --text-white: #f2f2f2;
  }
  * { box-sizing: border-box; margin: 0; padding: 0; }
  html, body {
    width: 1200px; height: 900px; overflow: hidden;
    background: var(--backdrop);
    font-family: "Montserrat", sans-serif;
  }
  .canvas {
    position: relative; width: 1200px; height: 900px;
  }
  .card {
    position: absolute; left: 294px;
    width: 612px; height: 350px;
    background: var(--card);
    box-shadow: 0 10px 28px rgba(0,0,0,.55);
  }
  .card--front { top: 70px; }
  .card--back { top: 480px; }

  .brand {
    display: flex; align-items: center; gap: 14px;
  }
  .brand__dot {
    width: 34px; height: 34px; border-radius: 50%;
    background: var(--brand-red);
  }
  .brand__name {
    font-weight: 800; color: var(--brand-red);
    text-transform: uppercase; letter-spacing: 3px;
    font-size: 34px; line-height: 1;
  }
  .card--front .brand {
    position: absolute; left: 50%; top: 50%;
    transform: translate(-50%, -50%);
  }
  .card--back .brand {
    position: absolute; right: 36px; top: 70px;
  }
  .card--back .brand__dot { width: 24px; height: 24px; }
  .card--back .brand__name { font-size: 24px; letter-spacing: 2px; }

  .holder {
    position: absolute; left: 42px; top: 160px;
  }
  .holder__name {
    color: var(--accent-blue); font-weight: 700;
    font-size: 28px; text-transform: uppercase; letter-spacing: -.5px;
    line-height: 1;
  }
  .holder__role {
    color: var(--text-white); font-weight: 300;
    font-size: 17px; margin-top: 4px;
  }
  .divider {
    position: absolute; left: 42px; right: 36px; top: 236px;
    height: 2px; background: var(--accent-blue);
  }
  .contacts {
    position: absolute; left: 42px; top: 254px;
    list-style: none;
  }
  .contacts__item {
    display: flex; align-items: center; gap: 16px;
    color: var(--text-white); font-size: 16px; font-weight: 400;
    height: 32px;
  }
  .contacts__icon { width: 20px; height: 20px; fill: var(--accent-blue); }
</style>
</head>
<body>
<main class="canvas">
  <section class="card card--front">
    <div class="brand">
      <span class="brand__dot"></span>
      <span class="brand__name">Brindle Crafts</span>
    </div>
  </section>

  <section class="card card--back">
    <div class="brand">
      <span class="brand__dot"></span>
      <span class="brand__name">Brindle Crafts</span>
    </div>

    <div class="holder">
      <h1 class="holder__name">Marcus Delgado</h1>
      <p class="holder__role">Owner</p>
    </div>

    <div class="divider"></div>

    <ul class="contacts">
      <li class="contacts__item">
        <svg class="contacts__icon" viewBox="0 0 24 24" aria-hidden="true">
          <path d="M6.6 10.8a15.1 15.1 0 0 0 6.6 6.6l2.2-2.2a1 1 0 0 1 1-.25 11.4 11.4 0 0 0 3.6.57 1 1 0 0 1 1 1V20a1 1 0 0 1-1 1A17 17 0 0 1 3 4a1 1 0 0 1 1-1h3.5a1 1 0 0 1 1 1c0 1.25.2 2.45.57 3.57a1 1 0 0 1-.25 1z"/>
        </svg>
        <span>321-555-0148</span>
      </li>
      <li class="contacts__item">
        <svg class="contacts__icon" viewBox="0 0 24 24" aria-hidden="true">
          <path d="M2 5h20v14H2z M3.5 6.5 12 13l8.5-6.5" fill="var(--accent-blue)" stroke="var(--card)" stroke-width="1.2"/>
        </svg>
        <span>brindlecrafts@mailbox.example</span>
      </li>
    </ul>
  </section>
</main>
</body>
</html>
```